General contractor/GM consaltant business card

I need a card for my contracting company in North Dakota, we build industrial buildings for the oil feild and oil feild related companies offices, shops, airplain hangars, airports ext. We have a familly atmosphere on the job and are very relational and personal.
Industry/Entity Type
Industrial
Contact Information for Business Card
Kestrelmoor Builders LLC.
Dwight T.Halvorsun
4736 Quillfern dr. Colorado Springs, CO. 80927
Cell# 406-555-8142
dwight@kestrelmoorbuilders.com

```html
<!DOCTYPE html>
<html lang="en">
<head>
<meta charset="utf-8">
<title>Kestrelmoor Builders LLC – Business Card</title>
<link rel="stylesheet" href="https://fonts.googleapis.com/css2?family=Arimo:wght@400;700&display=swap">
<style>
  :root {
    --bg: #1c1c1c;
    --card-light: #f4f4f4;
    --card-shade: #e2e2e2;
    --brand-blue: #17519a;
    --brand-navy: #0f3f7a;
    --accent-teal: #2499a9;
    --name-teal: #3aa9b9;
    --text-navy: #12417f;
    --photo-light: #d7d8b8;
    --photo-mid: #9d9e78;
    --photo-dark: #3f402c;
    --white: #ffffff;
  }
  * { box-sizing: border-box; margin: 0; padding: 0; }
  html, body {
    width: 1200px; height: 1000px; overflow: hidden;
    background: var(--bg);
    font-family: "Arimo", Arial, sans-serif;
  }
  .canvas {
    position: relative; width: 1200px; height: 1000px;
  }
  .card {
    position: absolute; left: 220px; width: 760px; height: 434px;
    overflow: hidden; box-shadow: 0 10px 30px rgba(0,0,0,.6);
  }
  /* Back side */
  .card--back { top: 44px; }
  .card-back__photo {
    position: absolute; inset: 0;
    background: radial-gradient(circle at 45% 70%, var(--photo-light) 0%, var(--photo-mid) 45%, var(--photo-dark) 100%);
  }
  .card-back__title {
    position: absolute; top: 34px; right: 40px;
    font-size: 46px; font-weight: 700; color: var(--white);
    white-space: nowrap;
    text-shadow: 0 0 8px rgba(255,255,255,.9), 0 0 2px #666;
  }
  /* Front side */
  .card--front { top: 522px;
    background: linear-gradient(120deg, var(--card-shade) 0%, var(--card-light) 35%, var(--white) 60%, var(--card-light) 100%);
  }
  .company-name {
    position: absolute; left: 36px; top: 156px; width: 380px;
    font-size: 29px; font-weight: 400; color: var(--brand-blue);
    white-space: nowrap;
    text-shadow: 2px 3px 3px rgba(0,0,0,.35);
  }
  .divider {
    position: absolute; left: 430px; top: 34px; width: 2px; height: 272px;
    background: var(--brand-navy);
  }
  .contact {
    position: absolute; left: 450px; top: 36px; right: 16px;
  }
  .contact__name {
    font-size: 26px; color: var(--name-teal); margin-left: 36px; margin-bottom: 22px;
    white-space: nowrap;
  }
  .contact__row {
    display: flex; align-items: center; gap: 14px; margin-bottom: 16px;
    font-size: 15px; color: var(--text-navy); line-height: 1.15;
  }
  .contact__icon {
    flex: 0 0 34px; width: 34px; height: 34px; border-radius: 6px;
    background: var(--brand-blue);
    display: flex; align-items: center; justify-content: center;
  }
  .band {
    position: absolute; left: 0; right: 0; bottom: 28px; height: 26px;
  }
</style>
</head>
<body>
<main class="canvas">

  <section class="card card--back" aria-label="Card back">
    <div class="card-back__photo" role="img" aria-label="Sepia-toned photo of construction workers silhouetted on a steel frame beside a crane lifting a truss over a city skyline"></div>
    <h2 class="card-back__title">Kestrelmoor Builders LLC</h2>
  </section>

  <section class="card card--front" aria-label="Card front">
    <h1 class="company-name">Kestrelmoor Builders LLC</h1>
    <div class="divider"></div>
    <div class="contact">
      <p class="contact__name">Dwight T.Halvorsun</p>
      <div class="contact__row">
        <span class="contact__icon">
          <svg width="18" height="22" viewBox="0 0 18 22"><path d="M9 1a7 7 0 0 0-7 7c0 5 7 13 7 13s7-8 7-13a7 7 0 0 0-7-7z" fill="#fff"/><circle cx="9" cy="8" r="2.6" fill="#17519a"/></svg>
        </span>
        <span>4736 Quillfern dr. Colorado Springs,<br>CO. 80927</span>
      </div>
      <div class="contact__row">
        <span class="contact__icon">
          <svg width="16" height="24" viewBox="0 0 16 24"><rect x="1" y="1" width="14" height="22" rx="2.5" fill="none" stroke="#fff" stroke-width="2"/><rect x="3.5" y="4" width="9" height="14" fill="#fff" opacity=".5"/><circle cx="8" cy="20.5" r="1" fill="#fff"/></svg>
        </span>
        <span>406-555-8142</span>
      </div>
      <div class="contact__row">
        <span class="contact__icon">
          <svg width="22" height="16" viewBox="0 0 22 16"><rect x="1" y="1" width="20" height="14" fill="none" stroke="#fff" stroke-width="1.8"/><path d="M1 1l10 8 10-8" fill="none" stroke="#fff" stroke-width="1.8"/></svg>
        </span>
        <span>dwight@kestrelmoorbuilders.com</span>
      </div>
      <div class="contact__row">
        <span class="contact__icon">
          <svg width="22" height="22" viewBox="0 0 22 22" fill="none" stroke="#fff" stroke-width="1.5"><circle cx="11" cy="11" r="9"/><ellipse cx="11" cy="11" rx="4" ry="9"/><path d="M2 11h18M3.5 6h15M3.5 16h15"/></svg>
        </span>
        <span>www.kestrelmoorbuilders.com</span>
      </div>
    </div>
    <svg class="band" viewBox="0 0 760 26" preserveAspectRatio="none" aria-hidden="true">
      <polygon points="0,0 486,0 498,13 486,26 0,26" fill="var(--brand-blue)"/>
      <polygon points="494,0 760,0 760,26 494,26 506,13" fill="var(--accent-teal)"/>
      <polyline points="488,2 499,13 488,24" fill="none" stroke="#fff" stroke-width="3"/>
    </svg>
  </section>

</main>
</body>
</html>
```